Gymnastics Schedule for our Junior Gymnastics program (for pre-school aged children)

We are wanting an updated version of our timetable for our Junior Gym program, I have attached a link to our website to align with branding, I have attached an old timetable as an example and our avatars we want to use. https://hpr.org.au/
Target Market(s)
We have created an avatar to give you an idea of target market: Marnie Holt- a 32 year old married mother of 2. she has a 4 year old and a 1 year old. she is a small business owner who works from home. She values learning and prgoression for her children in gymnastics as well as socialization, activeness and providing the best opportunities.
Industry/Entity Type
Children's Sport - Gymnastics
Other font styles liked:
- Franklin Gothic

```html
<!DOCTYPE html>
<html lang="en">
<head>
<meta charset="utf-8">
<title>Hollyridge Gymnastics Centre – 2025 Junior Gymnastics Timetable</title>
<link rel="stylesheet" href="https://fonts.googleapis.com/css2?family=Poppins:wght@600;700;800&family=Outfit:wght@400;500;700&family=Playfair+Display:wght@700&family=Sniglet&display=swap">
<style>
  :root {
    --navy: #04037f;
    --navy-deep: #02026e;
    --red: #e0161b;
    --ink: #2e2a27;
    --white: #ffffff;
    --illus-a: #d9c3a3;
    --illus-b: #3a66c9;
  }
  * { box-sizing: border-box; margin: 0; padding: 0; }
  html, body { width: 1200px; height: 848px; overflow: hidden; background: var(--white); }
  .sheet { position: relative; width: 1200px; height: 848px; font-family: "Outfit", sans-serif; color: var(--navy); }

  .brand { position: absolute; left: 40px; top: 62px; display: flex; align-items: center; gap: 8px; }
  .brand-dot { width: 16px; height: 16px; border-radius: 50%; background: var(--red); }
  .brand-name { font-family: "Outfit", sans-serif; font-weight: 700; font-size: 18px; line-height: 1.05; color: var(--navy); width: 120px; }
  .partner { position: absolute; background: var(--navy); }
  .partner--round { left: 196px; top: 42px; width: 56px; height: 56px; border-radius: 50%; }
  .partner--square { left: 290px; top: 46px; width: 54px; height: 64px; border-radius: 6px; background: #1f5fc0; }

  .club-name { position: absolute; left: 596px; top: 26px; font-family: "Poppins", sans-serif; font-weight: 700; font-size: 29px; color: var(--ink); letter-spacing: -0.3px; }
  .title { position: absolute; left: 410px; top: 56px; font-family: "Poppins", sans-serif; font-weight: 800; font-size: 60px; line-height: 1; color: var(--navy); letter-spacing: -1px; white-space: nowrap; }

  .rule { position: absolute; top: 164px; height: 2px; background: var(--navy); }
  .rule--left { left: 33px; width: 430px; }
  .rule--right { left: 737px; width: 430px; }
  .section-label { position: absolute; left: 463px; width: 274px; top: 145px; text-align: center; font-family: "Playfair Display", serif; font-weight: 700; font-size: 31px; letter-spacing: 9px; color: var(--red); padding-left: 9px; }

  .timetable { position: absolute; left: 33px; top: 189px; width: 1134px; display: grid; grid-template-columns: repeat(5, 224px); column-gap: 3.5px; }
  .day { display: flex; flex-direction: column; gap: 3px; }
  .day-head { height: 42px; background: var(--navy); color: var(--white); font-family: "Poppins", sans-serif; font-weight: 700; font-size: 23px; display: flex; align-items: center; justify-content: center; margin-bottom: 1px; }
  .slot { height: 33px; background: var(--navy); border-radius: 4px; color: var(--white); font-size: 19px; display: flex; align-items: center; justify-content: center; }

  .about { position: absolute; left: 53px; top: 546px; }
  .about h2 { font-family: "Poppins", sans-serif; font-weight: 700; font-size: 19px; color: var(--navy); margin-bottom: 5px; }
  .about ul { list-style: none; }
  .about li { position: relative; padding-left: 27px; font-size: 14.6px; color: var(--ink); line-height: 21px; margin-bottom: 5px; }
  .about li svg { position: absolute; left: 0; top: 4px; width: 14px; height: 14px; }

  .illustration { position: absolute; left: 790px; top: 520px; width: 378px; height: 250px; border-radius: 30px; background: linear-gradient(120deg, var(--illus-a), var(--illus-b)); opacity: 0.55; }

  .wave { position: absolute; left: 0; top: 0; width: 1200px; height: 848px; pointer-events: none; }
  .tagline { position: absolute; left: 0; width: 1200px; top: 790px; text-align: center; font-family: "Sniglet", sans-serif; font-size: 29px; color: var(--white); }
</style>
</head>
<body>
<main class="sheet">
  <div class="brand">
    <span class="brand-dot"></span>
    <span class="brand-name">Hollyridge Gymnastics</span>
  </div>
  <div class="partner partner--round" aria-hidden="true"></div>
  <div class="partner partner--square" aria-hidden="true"></div>

  <p class="club-name">Hollyridge Gymnastics Centre</p>
  <h1 class="title">2025 JUNIOR GYMNASTICS</h1>

  <span class="rule rule--left"></span>
  <span class="section-label">TIMETABLE</span>
  <span class="rule rule--right"></span>

  <section class="timetable">
    <div class="day">
      <div class="day-head">MONDAY</div>
      <div class="slot">9.30am – 10.20am</div><div class="slot">10.30am - 11.20am</div><div class="slot">11.30am - 12.20pm</div><div class="slot">2.00pm - 2.50pm</div>
      <div class="slot"></div><div class="slot"></div><div class="slot"></div><div class="slot"></div>
    </div>
    <div class="day">
      <div class="day-head">WEDNESDAY</div>
      <div class="slot">9.30am – 10.20am</div><div class="slot">10.30am - 11.20am</div><div class="slot">11.30am - 12.20pm</div><div class="slot">2.00pm - 2.50pm</div>
      <div class="slot"></div><div class="slot"></div><div class="slot"></div><div class="slot"></div>
    </div>
    <div class="day">
      <div class="day-head">THURSDAY</div>
      <div class="slot">9.30am – 10.20am</div><div class="slot">10.30am - 11.20am</div><div class="slot">11.30am - 12.20pm</div><div class="slot">2.00pm - 2.50pm</div>
      <div class="slot"></div><div class="slot"></div><div class="slot"></div><div class="slot"></div>
    </div>
    <div class="day">
      <div class="day-head">FRIDAY</div>
      <div class="slot">9.30am – 10.20am</div><div class="slot">10.30am - 11.20am</div><div class="slot">11.30am - 12.20pm</div><div class="slot">2.00pm - 2.50pm</div>
      <div class="slot"></div><div class="slot"></div><div class="slot"></div><div class="slot"></div>
    </div>
    <div class="day">
      <div class="day-head">SUNDAY</div>
      <div class="slot">9.00am - 9.50am</div><div class="slot">9.15am - 10.05am</div><div class="slot">10.00am - 10.50am</div><div class="slot">10.15am - 11.05am</div>
      <div class="slot">11.00am - 11.50am</div><div class="slot">11.15am - 12.05pm</div><div class="slot">12.00pm - 12.50pm</div><div class="slot">12.15pm - 1.05pm</div>
    </div>
  </section>

  <section class="about">
    <h2>ABOUT OUR PROGRAM</h2>
    <ul>
      <li><svg viewBox="0 0 14 14"><rect x="1" y="2" width="11" height="11" fill="none" stroke="#e0161b" stroke-width="1.6"/><path d="M4 7l3 3 6-8" fill="none" stroke="#e0161b" stroke-width="1.8"/></svg>Hollyridge Gymnastics is a 5-star Centre, as rated by Gym Sport National</li>
      <li><svg viewBox="0 0 14 14"><rect x="1" y="2" width="11" height="11" fill="none" stroke="#e0161b" stroke-width="1.6"/><path d="M4 7l3 3 6-8" fill="none" stroke="#e0161b" stroke-width="1.8"/></svg>Junior Gym is a structured program with an emphasis on fun and learning –<br>a program that grows with your child!</li>
      <li><svg viewBox="0 0 14 14"><rect x="1" y="2" width="11" height="11" fill="none" stroke="#e0161b" stroke-width="1.6"/><path d="M4 7l3 3 6-8" fill="none" stroke="#e0161b" stroke-width="1.8"/></svg>We teach gymnastics skills that can lead to improved co-ordination, balance and confidence</li>
      <li><svg viewBox="0 0 14 14"><rect x="1" y="2" width="11" height="11" fill="none" stroke="#e0161b" stroke-width="1.6"/><path d="M4 7l3 3 6-8" fill="none" stroke="#e0161b" stroke-width="1.8"/></svg>Suitable for children aged 2-5 years old (not yet attending school)</li>
      <li><svg viewBox="0 0 14 14"><rect x="1" y="2" width="11" height="11" fill="none" stroke="#e0161b" stroke-width="1.6"/><path d="M4 7l3 3 6-8" fill="none" stroke="#e0161b" stroke-width="1.8"/></svg>Parent assisted classes for 2-4 year olds, and non parent assisted classes for 4-5 year olds</li>
      <li><svg viewBox="0 0 14 14"><rect x="1" y="2" width="11" height="11" fill="none" stroke="#e0161b" stroke-width="1.6"/><path d="M4 7l3 3 6-8" fill="none" stroke="#e0161b" stroke-width="1.8"/></svg>All classes are led by our warm, friendly and qualified coaches and run for 50 minutes</li>
    </ul>
  </section>

  <div class="illustration" role="img" aria-label="Illustration of two cartoon child gymnasts, one balancing on one leg and one doing a cartwheel"></div>

  <svg class="wave" viewBox="0 0 1200 848" aria-hidden="true">
    <path d="M0 750 C200 790 500 786 800 768 C1000 756 1120 748 1200 782 L1200 848 L0 848 Z" fill="#e0161b"/>
    <path d="M0 758 C200 796 500 794 800 776 C1000 764 1120 758 1200 790 L1200 848 L0 848 Z" fill="#04037f"/>
  </svg>
  <p class="tagline">Hollyridge’s Junior Gym Program – Fun, Safe, Learning - A program that grows with your child</p>
</main>
</body>
</html>
```